card design for engineering consultancy

engineering drafting and project management company the provides drafting services for.
Electrical, Hydraulic, Mechanical, and Civil services
The company is called Q7R Services and logo is as attached
Information on card should be.
1. Logo
2.website : Q7RServices.example
3. email : info@Q7RServices.example
4. Phone: (+61) 400512836
5. Motto: Design - Document - Develop - Deliver

this card should be basically used for business identification only

Target Market(s)

electricians plumbers air conditioning installers and civil contractors

Industry/Entity Type

engineering, drafting, electrical, plumbing, airconditioning, civil

Contact Information for Business Card

1. Logo 2.website : Q7RServices.example 3. email : info@Q7RServices.example 4. Phone: (+61) 400512836 5. Motto: Design - Document - Develop - Deliver

Font styles to use
Serif

Requirements
Must have
• logo
Nice to have
• something inovative and different that makes it stand out from being just another business card

```html
<!DOCTYPE html>
<html lang="en">
<head>
<meta charset="utf-8">
<title>Q7R Services – Business Card</title>
<link rel="stylesheet" href="https://fonts.googleapis.com/css2?family=Montserrat:wght@400;500;600;700&display=swap">
<style>
  :root {
    --backdrop: #d6d6d8;
    --card-dark: #4a4a4c;
    --mark-dark: #2c2c2e;
    --card-light: #f7f7f7;
    --ink: #3d3d3f;
    --accent: #d41f2c;
    --band: #4a4a4c;
    --white: #ffffff;
  }
  * { box-sizing: border-box; margin: 0; padding: 0; }
  html, body {
    width: 1200px;
    height: 882px;
    overflow: hidden;
  }
  body {
    background: var(--backdrop);
    font-family: "Montserrat", sans-serif;
    position: relative;
  }
  .card {
    position: absolute;
    left: 290px;
    width: 620px;
    height: 353px;
    box-shadow: 0 3px 10px rgba(0,0,0,0.22);
    overflow: hidden;
  }
  .card--front {
    top: 70px;
    background: var(--card-dark);
  }
  .card--back {
    top: 459px;
    background: var(--card-light);
  }
  .front-wordmark {
    position: absolute;
    left: 0;
    right: 0;
    top: 148px;
    text-align: center;
    font-weight: 700;
    font-size: 40px;
    letter-spacing: 6px;
    color: var(--mark-dark);
  }
  .holder-name {
    position: absolute;
    left: 52px;
    top: 64px;
    font-weight: 600;
    font-size: 28px;
    color: var(--ink);
  }
  .holder-title {
    position: absolute;
    left: 53px;
    top: 99px;
    font-weight: 400;
    font-size: 14px;
    color: var(--accent);
  }
  .contact-list {
    position: absolute;
    left: 51px;
    top: 218px;
    list-style: none;
  }
  .contact-item {
    display: flex;
    align-items: center;
    height: 21px;
    font-size: 14px;
    color: var(--ink);
  }
  .contact-icon {
    width: 13px;
    height: 13px;
    margin-right: 10px;
    flex: none;
  }
  .back-wordmark {
    position: absolute;
    left: 330px;
    width: 260px;
    top: 172px;
    text-align: center;
    font-weight: 700;
    font-size: 21px;
    letter-spacing: 3px;
    color: var(--ink);
  }
  .base-band {
    position: absolute;
    left: 0;
    right: 0;
    bottom: 0;
    height: 25px;
    background: var(--band);
  }
  .motto-tag {
    position: absolute;
    left: 257px;
    top: 309px;
    width: 324px;
    height: 30px;
    background: var(--accent);
    border: 2px solid var(--white);
    border-top: none;
    border-radius: 0 0 8px 8px;
    color: var(--white);
    font-size: 14.5px;
    font-weight: 500;
    display: flex;
    align-items: center;
    justify-content: center;
    white-space: nowrap;
  }
</style>
</head>
<body>

  <section class="card card--front" aria-label="Card front">
    <div class="front-wordmark">Q7R SERVICES</div>
  </section>

  <section class="card card--back" aria-label="Card back">
    <h1 class="holder-name">Marten Oskell</h1>
    <p class="holder-title">Executive Director</p>

    <ul class="contact-list">
      <li class="contact-item">
        <svg class="contact-icon" viewBox="0 0 16 16" aria-hidden="true">
          <path d="M3.5 1.5l2.5 0 1 3.5-1.8 1.2a8 8 0 0 0 4.6 4.6L11 9l3.5 1v2.5c0 1-1 2-2 2C6.5 14.5 1.5 9.5 1.5 3.5c0-1 1-2 2-2z" fill="none" stroke="var(--accent)" stroke-width="1.6"/>
        </svg>
        (+61) 400512836
      </li>
      <li class="contact-item">
        <svg class="contact-icon" viewBox="0 0 16 16" aria-hidden="true">
          <rect x="1" y="3" width="14" height="10" fill="var(--accent)"/>
          <path d="M1 3l7 5.5L15 3M1 13l5-4.5M15 13l-5-4.5" fill="none" stroke="var(--white)" stroke-width="1.2"/>
        </svg>
        info@Q7RServices.example
      </li>
      <li class="contact-item">
        <svg class="contact-icon" viewBox="0 0 16 16" aria-hidden="true">
          <circle cx="8" cy="8" r="7" fill="var(--accent)"/>
          <path d="M1 8h14M8 1v14M8 1c-3 3.5-3 10.5 0 14M8 1c3 3.5 3 10.5 0 14M2.5 4.5h11M2.5 11.5h11" fill="none" stroke="var(--white)" stroke-width="0.9"/>
        </svg>
        www.Q7RServices.example
      </li>
    </ul>

    <div class="back-wordmark">Q7R SERVICES</div>

    <div class="base-band"></div>
    <div class="motto-tag">Design • Document • Develop • Deliver</div>
  </section>

</body>
</html>
```